Harbor Lane Group Bus Card Design

We need a business card for our law firm that specializes in intellectual property law (patents, trademarks, copyrights). We are called The Harbor Lane Group. We have a globe logo (attached) that is currently the back of our card. We like the back, but aren't married to it. I will also attach the front side of what we use now. The black background looks bad/cheap. We want something that looks sharp and modern. Thank you.

```html
<!DOCTYPE html>
<html lang="en">
<head>
<meta charset="utf-8">
<title>The Harbor Lane Group – Business Card</title>
<link href="https://fonts.googleapis.com/css2?family=Open+Sans:wght@400;600&display=swap" rel="stylesheet">
<style>
  :root {
    --stage: #3b322d;
    --card-top: #22364f;
    --card-bottom: #15233a;
    --card-edge: #2c4260;
    --white: #f4f6f9;
    --muted: #a9b8cc;
    --blue: #4f8fd6;
    --blue-light: #7fb1e6;
    --divider: rgba(255,255,255,.22);
  }
  * { margin: 0; padding: 0; box-sizing: border-box; }
  html, body {
    width: 1200px; height: 844px; overflow: hidden;
    background: var(--stage);
    font-family: "Open Sans", sans-serif;
    color: var(--white);
  }
  .stage {
    position: relative; width: 1200px; height: 844px;
    display: flex; align-items: center; justify-content: center; gap: 40px;
  }
  .card {
    position: relative; width: 540px; height: 309px;
    background: linear-gradient(160deg, var(--card-top), var(--card-bottom));
    border: 1px solid var(--card-edge);
    box-shadow: 0 12px 28px rgba(0,0,0,.45);
  }

  /* brand lockup */
  .brand { display: flex; align-items: center; gap: 12px; }
  .brand-mark { border-radius: 50%; background: var(--blue-light); flex: none; }
  .brand-name { font-weight: 600; letter-spacing: .5px; text-transform: uppercase; color: var(--white); white-space: nowrap; }
  .brand-tagline { color: var(--muted); letter-spacing: .5px; text-transform: uppercase; white-space: nowrap; }

  /* front */
  .card-front .brand { position: absolute; top: 38px; left: 0; right: 0; justify-content: center; }
  .card-front .brand-mark { width: 72px; height: 72px; }
  .card-front .brand-name { font-size: 17px; }
  .card-front .brand-tagline { font-size: 9.5px; margin-top: 4px; }

  .person { position: absolute; left: 38px; bottom: 40px; width: 210px; }
  .person-name { font-size: 22px; font-weight: 600; line-height: 1.1; }
  .person-title { font-size: 13px; color: var(--blue-light); margin-bottom: 14px; }
  .person-address { font-size: 14.5px; line-height: 1.3; }

  .divider { position: absolute; left: 262px; bottom: 42px; width: 1px; height: 100px; background: var(--divider); }

  .contact { position: absolute; left: 282px; bottom: 44px; list-style: none; }
  .contact li { display: flex; align-items: center; gap: 10px; font-size: 14px; height: 24px; }
  .contact-icon { width: 16px; height: 16px; background: var(--blue); border-radius: 2px; display: flex; align-items: center; justify-content: center; }

  /* back */
  .card-back { display: flex; flex-direction: column; align-items: center; justify-content: center; }
  .card-back .brand-mark { width: 90px; height: 90px; }
  .card-back .brand-name { font-size: 19px; }
  .card-back .brand-tagline { font-size: 10px; margin-top: 4px; }
  .website { margin-top: 26px; font-size: 11px; color: var(--muted); letter-spacing: .5px; }
</style>
</head>
<body>
<main class="stage">

  <section class="card card-front">
    <div class="brand">
      <span class="brand-mark"></span>
      <div>
        <div class="brand-name">The Harbor Lane Group</div>
        <div class="brand-tagline">Patents | Copyrights | Trademarks</div>
      </div>
    </div>

    <div class="person">
      <div class="person-name">Daniel Brooks</div>
      <div class="person-title">Managing Director</div>
      <div class="person-address">12345, Address Goes Here<br>Country Name, 123456</div>
    </div>

    <span class="divider"></span>

    <ul class="contact">
      <li><span class="contact-icon"><svg width="10" height="10" viewBox="0 0 10 10"><path d="M2 1l2 2-1 1.2c.6 1.2 1.6 2.2 2.8 2.8L7 6l2 2-1.2 1.2C4.6 9 1 5.4.8 2.2z" fill="#fff"/></svg></span>(044)-456-7890</li>
      <li><span class="contact-icon"><svg width="10" height="10" viewBox="0 0 10 10"><rect x="2.5" y=".5" width="5" height="9" rx="1" fill="#fff"/><rect x="3.5" y="1.8" width="3" height="5.5" fill="#4f8fd6"/></svg></span>123-456-7890</li>
      <li><span class="contact-icon"><svg width="10" height="10" viewBox="0 0 10 10"><rect x=".5" y="2" width="9" height="6" fill="#fff"/><path d="M.5 2L5 5.5 9.5 2" stroke="#4f8fd6" fill="none"/></svg></span>info@youremail.com</li>
      <li><span class="contact-icon"><svg width="10" height="10" viewBox="0 0 10 10"><path d="M4 6l2-2M3.5 4.5L2 6a1.4 1.4 0 002 2l1.5-1.5M6.5 5.5L8 4a1.4 1.4 0 00-2-2L4.5 3.5" stroke="#fff" stroke-width="1.2" fill="none"/></svg></span>www.website.com</li>
    </ul>
  </section>

  <section class="card card-back">
    <div class="brand">
      <span class="brand-mark"></span>
      <div>
        <div class="brand-name">The Harbor Lane Group</div>
        <div class="brand-tagline">Patents | Copyrights | Trademarks</div>
      </div>
    </div>
    <div class="website">WWW.HARBORLANE.COM</div>
  </section>

</main>
</body>
</html>
```